Business Card Design

We sell fish products to corporate food companies who then turn these products into final food products for consumers

Industry/Entity Type

Business

Contact Information for Business Card

I need a corporate business card template for a fish products business. We would like it be professional for use in dealing with multi national companies. This company business card template will be used by multiple employees so the following fields must be open to edit (Name, Phone Number and Email address)

```html
<!DOCTYPE html>
<html lang="en">
<head>
<meta charset="utf-8">
<title>Tidewell Seafoods – Business Card</title>
<link rel="stylesheet" href="https://fonts.googleapis.com/css2?family=Roboto:wght@300;400;700&display=swap">
<style>
  :root {
    --page-bg: #eceeef;
    --card-bg: #dde6ea;
    --wave-green: #6cc796;
    --wave-green-deep: #5bb983;
    --brand-blue: #2b6fb6;
    --brand-circle: #3a8fd0;
    --text-light: #ffffff;
    --card-shadow: rgba(40, 50, 60, 0.18);
  }
  * { box-sizing: border-box; margin: 0; padding: 0; }
  html, body {
    width: 1200px;
    height: 1000px;
    overflow: hidden;
    background: var(--page-bg);
    font-family: "Roboto", Arial, sans-serif;
  }
  .card {
    position: absolute;
    left: 150px;
    top: 243px;
    width: 900px;
    height: 514px;
    background: var(--card-bg);
    overflow: hidden;
    box-shadow: 0 18px 40px var(--card-shadow);
  }
  .card__wave {
    position: absolute;
    inset: 0;
    width: 100%;
    height: 100%;
  }
  .brand {
    position: absolute;
    left: 470px;
    top: 92px;
    display: flex;
    align-items: center;
    gap: 18px;
  }
  .brand__dot {
    width: 70px;
    height: 70px;
    border-radius: 50%;
    background: var(--brand-circle);
  }
  .brand__name {
    color: var(--brand-blue);
    font-weight: 400;
    font-size: 40px;
    line-height: 1;
    letter-spacing: 1px;
    text-transform: uppercase;
  }
  .contact {
    position: absolute;
    left: 110px;
    top: 342px;
    color: var(--text-light);
  }
  .contact__name {
    font-weight: 300;
    font-size: 38px;
    line-height: 1;
    letter-spacing: 1px;
  }
  .contact__role {
    font-weight: 700;
    font-size: 20px;
    margin-top: 4px;
  }
  .contact__list {
    list-style: none;
    margin-top: 14px;
    font-weight: 400;
    font-size: 17px;
  }
  .contact__item {
    display: flex;
    align-items: center;
    gap: 10px;
    margin-bottom: 8px;
  }
  .contact__icon {
    width: 16px;
    height: 16px;
    flex: none;
  }
</style>
</head>
<body>
  <main class="card">
    <svg class="card__wave" viewBox="0 0 900 514" preserveAspectRatio="none" aria-hidden="true">
      <defs>
        <linearGradient id="waveFill" x1="0" y1="1" x2="1" y2="0">
          <stop offset="0" stop-color="var(--wave-green-deep)"/>
          <stop offset="1" stop-color="var(--wave-green)"/>
        </linearGradient>
      </defs>
      <path d="M0 514 L0 470 C 50 360, 170 300, 340 292 C 540 282, 720 250, 900 120 L900 514 Z" fill="url(#waveFill)"/>
    </svg>

    <div class="brand">
      <span class="brand__dot" aria-hidden="true"></span>
      <span class="brand__name">Tidewell Seafoods</span>
    </div>

    <section class="contact">
      <h1 class="contact__name">JANE DOE</h1>
      <p class="contact__role">General Manager</p>
      <ul class="contact__list">
        <li class="contact__item">
          <svg class="contact__icon" viewBox="0 0 16 16" aria-hidden="true">
            <rect x="1" y="3" width="14" height="10" fill="none" stroke="#fff" stroke-width="1.4"/>
            <path d="M1 3 L8 9 L15 3" fill="none" stroke="#fff" stroke-width="1.4"/>
          </svg>
          <span>JaneDoe@tidewellseafoods.com</span>
        </li>
        <li class="contact__item">
          <svg class="contact__icon" viewBox="0 0 16 16" aria-hidden="true">
            <path d="M4 1.5 L6.5 4.5 L5 6.5 C6 8.5 7.5 10 9.5 11 L11.5 9.5 L14.5 12 L12.5 14.5 C7 14 2 9 1.5 3.5 Z" fill="#fff"/>
          </svg>
          <span>+ 0000 000 0000</span>
        </li>
      </ul>
    </section>
  </main>
</body>
</html>
```